Design a Pull Up Banner for a Coffee Business

We want to make a pull-up banner to be placed beside our mobile espresso bar in every events. The purpose of the banner is to attract attention and to make encourage customers to hire us for their events.

Business name is " Bean Harbor Company".
The slogan of our business is " Solutions to Great Coffee"
The main service we wanted to promote is " Events".

What is the "Events" Service about?
We call the service "Drop-in Espresso". Drop-in Espresso is a mobile espresso bar, where we can pop-up/set-up almost anywhere, for any events.
eg. Company Grand Opening, New Product Launch, Fashion Show, Wedding Reception etc...

NO Wordy Banner. NO Boring banner. NO Unrelated info.
WANT Catchy Phrases. WANT Appealing Photos. WANT Attract Attention.

Attached : Pictures of an event (Company Grand Opening) by B4 + B4 Logo

Updated with some pictures. Can take a look... Use them wisely. Simplicity, Attractive, Pleasant and most importantly, covey the right message, is the key.

Add this campaign name to the banner design...
"Treat Your Guest To The Best"

Main marketing element >Events<
Types of Events > Wedding Reception, Grand Opening, Product Launch, Corporate Event, Road Show etc etc

Please add our website in the design. "www.beanharborcompany.example"
Also social media.
Friendfold
Chirpline
Snapframe

```html
<!DOCTYPE html>
<html lang="en">
<head>
<meta charset="utf-8">
<title>Bean Harbor Company – Pull-up Banner</title>
<link rel="stylesheet" href="https://fonts.googleapis.com/css2?family=Oswald:wght@600&family=Rosarivo&family=Questrial&family=Advent+Pro:wght@200;300&display=swap">
<style>
  :root {
    --bg-light: #c7ad86;
    --bg-dark: #9d8260;
    --strip: #b39872;
    --panel: #d8c4a2;
    --band-brown: #7a3e1f;
    --ink: #111;
    --photo-warm: #8a5a3a;
    --photo-dark: #2b2523;
    --photo-cream: #e9e2da;
  }
  * { margin: 0; padding: 0; box-sizing: border-box; }
  html, body { width: 1200px; height: 2624px; overflow: hidden; }
  body { position: relative; font-family: "Questrial", sans-serif; color: var(--ink); }

  .backdrop {
    position: absolute; inset: 0;
    background:
      radial-gradient(ellipse 520px 420px at 740px 260px, rgba(240,225,200,.45), transparent 70%),
      radial-gradient(ellipse 520px 360px at 520px 2380px, rgba(240,225,200,.35), transparent 70%),
      linear-gradient(180deg, var(--bg-light), var(--bg-dark) 50%, var(--bg-light));
  }

  .brand { position: absolute; left: 93px; top: 96px; white-space: nowrap; }
  .brand-mark { width: 34px; height: 34px; background: var(--ink); margin-bottom: 62px; }
  .brand-name { font-family: "Oswald", sans-serif; font-weight: 600; font-size: 56px; line-height: 1; letter-spacing: -0.5px; }
  .brand-sub { font-family: "Oswald", sans-serif; font-weight: 600; font-size: 26px; line-height: 1.2; }

  .slogan { position: absolute; left: 435px; top: 160px; font-family: "Rosarivo", serif; font-size: 53px; letter-spacing: 1px; white-space: nowrap; }

  .band { position: absolute; left: 0; width: 1200px; }
  .band svg { display: block; }
  .band-text {
    position: absolute; left: 0; right: 0; text-align: center; white-space: nowrap;
    font-family: "Advent Pro", sans-serif; font-weight: 300;
  }
  .campaign { top: 365px; height: 195px; }
  .campaign .band-text { top: 24px; font-size: 84px; line-height: .86; letter-spacing: 1px; }
  .contact { top: 2056px; height: 192px; }
  .contact .band-text { top: 42px; font-size: 82px; line-height: .95; letter-spacing: 1px; }

  .strip { position: absolute; left: 0; width: 1200px; height: 36px; background: var(--strip); border-top: 2px solid #a88c66; border-bottom: 2px solid #a88c66; }

  .row { position: absolute; left: 0; width: 1200px; display: flex; }
  .row .photo { height: 100%; }
  .row .panel { flex: 1; background: var(--panel); }
  .row-one { top: 596px; height: 450px; }
  .row-one .photo { width: 620px; }
  .row-two { top: 1080px; height: 460px; }
  .row-two .panel { flex: 0 0 621px; }
  .row-two .photo { width: 579px; }
  .row-three { top: 1576px; height: 448px; }
  .row-three .photo { width: 620px; }

  .photo-hands { background: radial-gradient(circle at 45% 45%, var(--photo-cream) 0 14%, var(--photo-warm) 30%, var(--photo-dark) 85%); }
  .photo-pour { background: radial-gradient(ellipse at 55% 90%, var(--photo-cream) 0 18%, #6c5a50 30%, var(--photo-dark) 75%); }
  .photo-beans { background: linear-gradient(180deg, #1e2430 0 20%, #d9d6d2 22%, #b8a89a 55%, #3a2418 80%); }

  .service-lead { padding: 74px 0 0 0; text-align: center; font-size: 52px; letter-spacing: 2px; line-height: 1.45; white-space: nowrap; }
  .service-lead .events { display: block; margin-top: 22px; font-size: 110px; line-height: 1; letter-spacing: 0; }

  .event-list { list-style: none; font-size: 66px; line-height: 107px; word-spacing: 10px; white-space: nowrap; }
  .row-two .event-list { padding: 56px 0 0 14px; }
  .row-three .event-list { padding: 40px 0 0 20px; }

  .website { position: absolute; left: 0; right: 0; top: 2298px; text-align: center; font-family: "Advent Pro", sans-serif; font-weight: 300; font-size: 66px; white-space: nowrap; }

  .socials { position: absolute; left: 0; right: 0; top: 2440px; display: flex; justify-content: center; gap: 44px; list-style: none; font-size: 34px; }
  .socials li { display: flex; align-items: center; gap: 12px; }
  .socials .dot { width: 26px; height: 26px; background: var(--ink); }

  .brand-small { position: absolute; left: 1000px; top: 2500px; width: 170px; text-align: center; white-space: nowrap; }
  .brand-small .brand-name { font-size: 26px; letter-spacing: 0; }
  .brand-small .brand-sub { font-size: 12px; }
</style>
</head>
<body>
  <div class="backdrop" role="img" aria-label="Soft sepia close-up of a latte with heart-shaped milk foam art"></div>

  <header class="brand">
    <div class="brand-mark"></div>
    <div class="brand-name">BEAN HARBOR</div>
    <div class="brand-sub">COMPANY</div>
  </header>
  <p class="slogan">Solution To Great COFFEE</p>

  <section class="band campaign">
    <svg width="1200" height="195" viewBox="0 0 1200 195">
      <polygon points="0,172 128,172 290,0 915,0 1075,172 1200,172 1200,195 0,195" fill="#111"/>
      <polygon points="148,181 300,12 905,12 1060,181" fill="var(--band-brown)"/>
    </svg>
    <h1 class="band-text">Treat your Guest<br>to the Best</h1>
  </section>

  <div class="strip" style="top:560px"></div>
  <section class="row row-one">
    <div class="photo photo-hands" role="img" aria-label="Hands holding a cup of black coffee beside pastries"></div>
    <div class="panel">
      <p class="service-lead">DROP-IN ESPRESSO<br>FOR ANY<span class="events">“EVENTS”</span></p>
    </div>
  </section>

  <div class="strip" style="top:1045px"></div>
  <section class="row row-two">
    <div class="panel">
      <ul class="event-list"><li>Corporate Events</li><li>Fashion Show</li><li>Birthday</li></ul>
    </div>
    <div class="photo photo-pour" role="img" aria-label="Espresso pouring from a machine spout into a white cup"></div>
  </section>

  <div class="strip" style="top:1540px"></div>
  <section class="row row-three">
    <div class="photo photo-beans" role="img" aria-label="Espresso cup on a saucer with scattered coffee beans and star anise"></div>
    <div class="panel">
      <ul class="event-list"><li>Product Launch</li><li>Road Show</li><li>Wedding</li></ul>
    </div>
  </section>

  <section class="band contact">
    <svg width="1200" height="192" viewBox="0 0 1200 192">
      <polygon points="0,0 1200,0 1200,22 1075,22 915,192 290,192 128,22 0,22" fill="#111"/>
      <polygon points="148,12 1060,12 905,180 300,180" fill="var(--band-brown)"/>
    </svg>
    <h2 class="band-text">Contact Us</h2>
  </section>

  <p class="website">www.beanharborcompany.example</p>

  <ul class="socials">
    <li><span class="dot"></span>Friendfold</li>
    <li><span class="dot"></span>Chirpline</li>
    <li><span class="dot"></span>Snapframe</li>
  </ul>

  <footer class="brand-small">
    <div class="brand-name">BEAN HARBOR</div>
    <div class="brand-sub">COMPANY</div>
  </footer>
</body>
</html>
```